Zielgruppe
Wir sind ein Business Center und vermieten Büro- und Konferenzräume. Wir richten uns an Unternehmen unterschiedlichster Branchen: Freelancer ohne eigenes Büro oder auch große Unternehmen, welche keine eigene freien Vakanzen haben, z. B. für Vorstellungsgespräche.
Aufgabenstellung
Flyer Din Lang, quer, gebunden an der kurzen Seite. 8 Seiten, inkl. Vorder- und Rückseite. Bitte kein Wickelfalz oder ähnliches, sondern eine Broschüre, gebunden mit Klammerheftung!!!
Frisches helles Design, ohne Schnörkel. Bilder mit etwas Text, dazu eine Seite über uns. Rückseite Kontaktdaten. Je eine Doppelseite für Konferenzraumvermietung und eine Doppelseite für Büroraum auf Zeit, eine Doppelseite für unsere weitere Leistungen, Telefonservice (Anrufannahme im namen unserer Kunden).
Unsere Räume sind sehr repräsentativ und modern eingerichtet mit hellen Designermöbeln. Das soll auch in der Broschüre klar werden.

```html
<!DOCTYPE html>
<html lang="de">
<head>
<meta charset="utf-8">
<title>VELOFFICE Broschüre</title>
<link href="https://fonts.googleapis.com/css2?family=Arimo:wght@400;700&display=swap" rel="stylesheet">
<style>
:root{
  --green:#c8dc52;
  --green-line:#c5db4b;
  --ink:#333333;
  --paper:#ffffff;
  --stage:#f0f0f0;
  --shade:#e6e6e6;
}
*{box-sizing:border-box;margin:0;padding:0}
html,body{width:840px;height:1200px;overflow:hidden;background:var(--stage)}
body{font-family:"Arimo",Arial,sans-serif;color:var(--ink)}
.sheet{position:absolute;left:0;top:0;width:1607px;height:2296px;transform:scale(0.52271);transform-origin:0 0}
.abs{position:absolute}
.page{position:absolute;background:var(--paper);box-shadow:0 2px 6px rgba(0,0,0,.12)}
.page--right{background:linear-gradient(90deg,#e9e9e9 0,#fafafa 60px,#fff 140px)}
.photo{position:absolute}
.frame{position:absolute;border:4px solid var(--green-line)}
.heading{position:absolute;font-size:27px;line-height:32px;font-weight:400;text-transform:uppercase;letter-spacing:.2px}
.heading .accent{color:var(--green)}
.heading .gap{background:var(--paper);padding:0 10px;margin-left:-10px}
.body-text{position:absolute;font-size:13.4px;line-height:15.4px}
.checks{position:absolute;list-style:none;font-size:10.3px;line-height:12px}
.checks li{position:relative;padding-left:26px;margin-bottom:8px}
.checks li::before{content:"";position:absolute;left:4px;top:-1px;width:6px;height:11px;border:solid var(--green);border-width:0 3px 3px 0;transform:rotate(45deg)}
.logo{position:absolute;display:flex;align-items:center;gap:12px;font-weight:700;letter-spacing:1px;color:var(--ink)}
.logo .mark{width:16px;height:16px;background:var(--green)}
.price-table{position:absolute;border-collapse:collapse;font-size:13.2px}
.price-table td{padding:6px 0 4px;border-bottom:1.5px solid var(--green-line);vertical-align:top}
.price-table .col-unit{width:118px}
.price-table .col-val{width:34px;text-align:right}
.price-table .group td{font-weight:700;font-size:14.5px;padding:14px 0 8px}
.side-menu{position:absolute;list-style:none;color:#fff;font-size:13px;line-height:15px}
.side-menu li{position:relative;padding-left:24px;margin-bottom:9.3px}
.side-menu li::before{content:"→";position:absolute;left:0;top:0;color:#fff}
.service{position:absolute;width:200px;color:#fff;font-size:12.5px;line-height:15px}
.service h3{color:var(--ink);font-size:13px;font-weight:700;margin-bottom:10px}
.service svg{position:absolute;left:-42px;top:-4px}
.contact{position:absolute;list-style:none;color:var(--ink);font-size:13px}
.contact li{display:flex;align-items:center;gap:12px;height:24.3px}
</style>
</head>
<body>
<div class="sheet">

  <!-- Cover -->
  <section class="page cover" style="left:374px;top:70px;width:759px;height:380px;background:var(--green);box-shadow:none">
    <div class="abs" style="left:24px;top:24px;width:712px;height:333px;background:var(--paper)"></div>
    <div class="logo" style="left:70px;top:88px;font-size:42px"><span class="mark"></span>VELOFFICE</div>
    <h1 class="abs" style="left:55px;top:235px;font-size:27px;line-height:32px;font-weight:400">WILLKOMMEN<br>IN IHREM<br>NEUEN <span style="color:var(--green)">VELOFFICE!</span></h1>
    <div class="photo" role="img" aria-label="Schreibtisch von oben mit Monitor, Tastatur, Maus, Notizblock und Stift" style="left:371px;top:80px;width:320px;height:200px;background:radial-gradient(ellipse at 50% 40%,#e8e8e8,#fff 70%)"></div>
  </section>

  <!-- Spread 1: Konferenzraum -->
  <section class="page" style="left:44px;top:511px;width:759px;height:379px">
    <div class="photo" role="img" aria-label="Empfangstresen aus Holz" style="left:18px;top:18px;width:188px;height:101px;background:linear-gradient(180deg,#d7d3cc,#9c7652)"></div>
    <div class="photo" role="img" aria-label="Konferenztisch mit Bildschirm an der Wand" style="left:18px;top:134px;width:188px;height:227px;background:linear-gradient(180deg,#e2e2e0,#c9c6c0 60%,#5e4a3c)"></div>
    <div class="photo" role="img" aria-label="Heller Konferenzraum mit langem Tisch, Stühlen und Fenstern" style="left:221px;top:18px;width:521px;height:343px;background:linear-gradient(180deg,#eceae6,#dcd8d1 55%,#bfb1a0)"></div>
  </section>
  <section class="page page--right" style="left:805px;top:511px;width:758px;height:379px">
    <div class="frame" style="left:53px;top:36px;width:152px;height:307px"></div>
    <h2 class="heading" style="left:75px;top:66px"><span class="accent gap">Konferenzraum anmieten</span><br><span class="gap">in Düsseldorf</span></h2>
    <p class="body-text" style="left:228px;top:157px;width:312px">Nutzen Sie unsere modernen Konferenz- und Tagungsräume für Meetings, Präsentationen, Gespräche, oder Schulungen. Unsere hellen, stylischen Räume werden auch Sie faszinieren. Präsentieren Sie sich vor Ihren Geschäftspartnern an einem tollen Ort. Unser Team erfüllt all Ihre Wünsche - vom leckeren Cappuccino bishin zu raffinierten Canapes.</p>
    <ul class="checks" style="left:555px;top:58px;width:170px">
      <li>bis zu 10 Teilnehmer</li>
      <li>bekannte Location im Lindenhaus (Autohaus)</li>
      <li>persönlicher Empfang &amp; Betreuung</li>
      <li>55 Zoll 4k Fernseher</li>
      <li>Streaming-Box</li>
      <li>Bildschirmfreigabe</li>
      <li>Konferenztelefon</li>
      <li>großes Whiteboard</li>
      <li>Flipchart</li>
      <li>Tiefgarage</li>
    </ul>
  </section>

  <!-- Spread 2: Büroanmietung -->
  <section class="page" style="left:44px;top:947px;width:759px;height:380px">
    <div class="photo" role="img" aria-label="Tisch mit Pflanze und Glasleuchten vor heller Tür" style="left:20px;top:18px;width:182px;height:343px;background:linear-gradient(180deg,#dcd9cf,#c9c0a5 60%,#d6a35b)"></div>
    <div class="frame" style="left:220px;top:38px;width:318px;height:88px"></div>
    <h2 class="heading" style="left:256px;top:69px"><span class="accent">Büroanmietung</span><br><span class="gap">in Düsseldorf</span></h2>
    <p class="body-text" style="left:220px;top:184px;width:320px">Nach Vertragsunterzeichnung können Sie sofort einziehen: kein Umbau, keine Renovierung und wenn Sie wünschen, können Sie das Mietverhältnis kurzfristig wieder kündigen. Soviel Flexibiltät erhalten Sie nur bei uns!</p>
    <ul class="checks" style="left:553px;top:60px;width:160px">
      <li>Zugang 24/7</li>
      <li>persönlicher Empfang</li>
      <li>ab 15qm</li>
      <li>eigenes Firmenschild</li>
      <li>wöchentliche Reinigung inklusive</li>
      <li>kostenfreier Hochgeschwind-igkeits-Internetzugang</li>
      <li>große Schreibtische</li>
      <li>auf Wunsch inkl. Anrufan-nahme durch unser geschul-tes Personal</li>
      <li>optionale Anmietung eines Konferenzraumes mit bis zu 10 Plätzen</li>
      <li>Mitbenutzung der sanitären Einrichtungen und der Küche</li>
    </ul>
  </section>
  <section class="page page--right" style="left:805px;top:950px;width:758px;height:380px;background:var(--paper)">
    <div class="photo" role="img" aria-label="Schreibtisch mit Laptop, Stehlampe und Bürostuhl" style="left:14px;top:17px;width:521px;height:348px;background:linear-gradient(180deg,#e4e2de,#d5d2cc 70%,#eeeeec)"></div>
    <div class="photo" role="img" aria-label="Bürogebäude an einer Straße mit Straßenbahn" style="left:550px;top:17px;width:192px;height:103px;background:linear-gradient(180deg,#e8ecef,#b5b9bb 60%,#7d7a74)"></div>
    <div class="photo" role="img" aria-label="Schwarzer Sessel mit Pflanze" style="left:550px;top:136px;width:192px;height:111px;background:linear-gradient(180deg,#e6e6e3,#6c6c6a 60%,#2b2b2b)"></div>
    <div class="photo" role="img" aria-label="Kaffeemaschine mit Tasse" style="left:550px;top:263px;width:192px;height:102px;background:linear-gradient(90deg,#2a2a2a,#d9d6d0 50%,#2e2e2e)"></div>
  </section>

  <!-- Spread 3: Telefonservice & Preise -->
  <section class="page" style="left:44px;top:1388px;width:759px;height:380px">
    <div class="frame" style="left:54px;top:37px;width:318px;height:89px"></div>
    <h2 class="heading" style="left:89px;top:72px"><span class="accent">Telefonservice</span><br><span class="gap">ClearCall</span></h2>
    <div class="abs" style="left:552px;top:37px;width:153px;height:152px;background:var(--green);color:#fff;font-size:13.2px;line-height:16.8px;padding:30px 22px 0">Mit ClearCall haben Sie einen entscheidenden Vorteil: <b>Erreichbarkeit!</b></div>
    <p class="body-text" style="left:54px;top:159px;width:485px;font-size:12.6px;line-height:15px">Ihre Anrufer werden begeistert sein, dass Sie ab sofort durchgängig erreichbar sind. Verzichten Sie zukünftig auf einen unpersönlichen Anrufbeantworter oder die Rufum-leitung auf Ihr Mobilfunktelefon.</p>
    <ul class="checks" style="left:54px;top:226px;width:330px;font-size:10px">
      <li>Annahmezeiten: Mo.-Fr. 08:00 - 20:00 Uhr (individuell anpassbar)</li>
      <li>pauschale Abrechnung mit 1,00 Euro pro Anruf</li>
      <li>Anrufannahme mit Ihrem Firmennamen</li>
      <li>Abfrage von Name, Anrufgrund (in Form eines Stichwortes), Rufnummer, ggf. Emailadresse</li>
      <li>auf Wunsch Vermittlung an den gewünschten Ansprechpartner</li>
    </ul>
    <ul class="checks" style="left:387px;top:226px;width:320px;font-size:10px">
      <li>deutsch- und englischsprachige Mitarbeiter</li>
      <li>ISDN Technologie - KEIN VOIP</li>
      <li>individuelle Einstellmöglichkeiten auf Mein VELOFFICE</li>
      <li>inkl. Anrufbeantworter</li>
      <li>Firmensitz: Düsseldorf</li>
      <li>mtl. kündbar</li>
    </ul>
  </section>
  <section class="page page--right" style="left:805px;top:1388px;width:758px;height:380px">
    <h2 class="heading" style="left:53px;top:72px"><span class="accent">Preise</span> - Tarif ClearCall<sup style="font-size:15px">1</sup></h2>
    <div class="abs" style="left:338px;top:116px;font-size:10px">Euro</div>
    <table class="price-table" style="left:53px;top:128px;width:318px">
      <tr><td>Grundgebühr</td><td class="col-unit">pro Monat</td><td class="col-val">29,95</td></tr>
      <tr><td>Anrufannahme</td><td class="col-unit">pro Anruf</td><td class="col-val">1,00</td></tr>
      <tr><td>Benachrichtigung</td><td class="col-unit">pro Mail</td><td class="col-val"></td></tr>
      <tr class="group"><td colspan="3">optional, sofern Sie dies wünschen</td></tr>
      <tr><td>Weiterleiten in Ihr dt.<br>Festnetz</td><td class="col-unit">pro Minute</td><td class="col-val">0,04</td></tr>
      <tr><td>Weiterleiten in Ihr dt.<br>Mobilnetz</td><td class="col-unit">pro Minute</td><td class="col-val">0,20</td></tr>
      <tr><td>SMS Benachrichtigung</td><td class="col-unit">pro SMS</td><td class="col-val">0,12</td></tr>
    </table>
    <p class="abs" style="left:382px;top:308px;width:150px;font-size:9.6px;line-height:11.5px">1) Vertragslaufzeit auf unbestim-mte Zeit, 7 Werktage vor Monatsende kündbar</p>
    <div class="abs" style="left:549px;top:0;width:209px;height:380px;background:var(--green)"></div>
    <div class="logo" style="left:572px;top:54px;font-size:23px;gap:8px"><span class="mark" style="width:10px;height:10px;background:#fff"></span>VELOFFICE</div>
    <ul class="side-menu" style="left:570px;top:143px;width:130px">
      <li>Leistungen Telefonservice</li>
      <li>Bürovermietung</li>
      <li>Telefonsekretariat</li>
      <li>Telefonannahme</li>
      <li>Virtual Office</li>
      <li>Telefonzentrale</li>
      <li>Büroservice</li>
      <li>Call Center</li>
    </ul>
  </section>

  <!-- Back cover -->
  <section class="page back" style="left:447px;top:1833px;width:759px;height:379px;background:var(--green);box-shadow:none">
    <div class="service" style="left:95px;top:57px">
      <svg width="22" height="22" viewBox="0 0 24 24" aria-hidden="true"><path fill="#fff" d="M6.6 10.8a15 15 0 0 0 6.6 6.6l2.2-2.2a1 1 0 0 1 1-.25 11.4 11.4 0 0 0 3.6.57 1 1 0 0 1 1 1V20a1 1 0 0 1-1 1A17 17 0 0 1 3 4a1 1 0 0 1 1-1h3.5a1 1 0 0 1 1 1c0 1.25.2 2.45.57 3.57a1 1 0 0 1-.25 1z"/></svg>
      <h3>Telefonservice</h3>ClearCall Sekretariatsservice, schon ab 1,00 Euro/Anruf</div>
    <div class="service" style="left:314px;top:57px">
      <svg width="24" height="24" viewBox="0 0 24 24" aria-hidden="true"><circle cx="8" cy="8" r="5" fill="none" stroke="#fff" stroke-width="2.5"/><path d="M11.5 11.5 20 20m-3-3 2-2m-4 0 2-2" stroke="#fff" stroke-width="2.5" fill="none"/></svg>
      <h3>Exklusive Büroanmietung</h3>hochwertig, provisionsfrei und repräsentativ in bester Lage</div>
    <div class="service" style="left:537px;top:57px">
      <svg width="24" height="26" viewBox="0 0 24 26" aria-hidden="true"><rect x="2" y="8" width="20" height="16" rx="2" fill="#fff"/><rect x="6" y="2" width="12" height="8" fill="#fff"/><g fill="var(--green)"><rect x="8" y="13" width="2" height="2"/><rect x="12" y="13" width="2" height="2"/><rect x="16" y="13" width="2" height="2"/><rect x="8" y="17" width="2" height="2"/><rect x="12" y="17" width="2" height="2"/><rect x="16" y="17" width="2" height="2"/></g></svg>
      <h3>ClearNumbers</h3>Ihre neue Düsseldorfer Ruf- und Faxnummer</div>
    <div class="service" style="left:95px;top:143px">
      <svg width="26" height="22" viewBox="0 0 26 22" aria-hidden="true"><rect x="1" y="5" width="24" height="16" rx="2" fill="#fff"/><rect x="9" y="1" width="8" height="5" fill="none" stroke="#fff" stroke-width="2"/><rect x="1" y="11" width="24" height="2" fill="var(--green)"/></svg>
      <h3>Virtual Office</h3>Zeigen Sie Präsenz in der Landeshauptstadt Düsseldorf</div>
    <div class="service" style="left:314px;top:143px">
      <svg width="26" height="24" viewBox="0 0 26 24" aria-hidden="true"><rect x="2" y="5" width="16" height="17" rx="2" fill="none" stroke="#fff" stroke-width="2.2"/><path d="M9 15 22 2l2 2-13 13H9z" fill="#fff"/></svg>
      <h3>Hotline</h3>First-Level-Support, Bestellan-nahme u.v.m.</div>
    <div class="service" style="left:537px;top:143px">
      <svg width="28" height="22" viewBox="0 0 28 22" aria-hidden="true"><g fill="#fff"><circle cx="14" cy="6" r="4.5"/><circle cx="5" cy="8" r="3.3"/><circle cx="23" cy="8" r="3.3"/><path d="M6 21c0-5 3.5-8 8-8s8 3 8 8z"/><path d="M0 19c0-4 2.2-6 5-6 1 0 2 .3 2.6.8A9 9 0 0 0 4.6 19z"/><path d="M28 19c0-4-2.2-6-5-6-1 0-2 .3-2.6.8a9 9 0 0 1 3 5.2z"/></g></svg>
      <h3>Termine</h3>Wir arbeiten u. a. mit terminio, Planwerk und Kalendra</div>
    <div class="logo" style="left:60px;top:280px;font-size:33px"><span class="mark" style="background:#fff"></span>VELOFFICE</div>
    <ul class="contact" style="left:411px;top:253px">
      <li><svg width="14" height="16" viewBox="0 0 14 18" aria-hidden="true"><path fill="#fff" d="M7 0a7 7 0 0 0-7 7c0 5 7 11 7 11s7-6 7-11a7 7 0 0 0-7-7zm0 9.5A2.5 2.5 0 1 1 7 4.5a2.5 2.5 0 0 1 0 5z"/></svg>Lindenweg 112-118, 40235 Düsseldorf</li>
      <li><svg width="14" height="14" viewBox="0 0 14 14" aria-hidden="true"><circle cx="7" cy="7" r="7" fill="#fff"/><path d="M7 3v4l3 2" stroke="var(--green)" stroke-width="1.6" fill="none"/></svg>Mo.-Fr. 08:00 - 20:00</li>
      <li><svg width="14" height="14" viewBox="0 0 24 24" aria-hidden="true"><path fill="#fff" d="M6.6 10.8a15 15 0 0 0 6.6 6.6l2.2-2.2a1 1 0 0 1 1-.25 11.4 11.4 0 0 0 3.6.57 1 1 0 0 1 1 1V20a1 1 0 0 1-1 1A17 17 0 0 1 3 4a1 1 0 0 1 1-1h3.5a1 1 0 0 1 1 1c0 1.25.2 2.45.57 3.57a1 1 0 0 1-.25 1z"/></svg>0800 - 4 207 319</li>
      <li><svg width="14" height="11" viewBox="0 0 14 11" aria-hidden="true"><rect width="14" height="11" rx="1" fill="#fff"/><path d="M0 1l7 5 7-5" stroke="var(--green)" stroke-width="1.4" fill="none"/></svg>info@veloffice.de</li>
    </ul>
  </section>

</div>
</body>
</html>
```